Banner Design for High End Jewelry Website

We need a banner for our website (brindlestone.com) for a sale that we will be running. The banner should be a size 1187 × 400. I have included a few pieces of jewelry to be included in the banner (do not need to use all, can use just some). The banner should say:
"Christmas is Closer Than You Think Sale!"
Shop Now

Industry/Entity Type

Jewelry

```html
<!DOCTYPE html>
<html lang="en">
<head>
<meta charset="utf-8">
<title>Brindlestone — Fine Estate and Designer Jewelry</title>
<link href="https://fonts.googleapis.com/css2?family=Oswald:wght@400;600;700&family=Great+Vibes&family=Open+Sans:wght@400;600&display=swap" rel="stylesheet">
<style>
  :root {
    --page: #ffffff;
    --ink: #2a2a2a;
    --muted: #8a8a8a;
    --tan: #a89483;
    --tan-light: #d9c9bc;
    --tan-pale: #efe6de;
    --blush: #f1dcd5;
    --blush-deep: #e7c6bb;
    --crimson: #a3192c;
    --crimson-dark: #7f1021;
    --gold: #d9b56a;
  }
  * { box-sizing: border-box; margin: 0; padding: 0; }
  html, body { width: 1200px; height: 1200px; overflow: hidden; background: var(--page); }
  body { font-family: "Open Sans", sans-serif; color: var(--ink); position: relative; }

  .sign-up-corner { position: absolute; top: 0; right: 0; width: 90px; height: 90px; }

  .site { width: 1000px; margin: 0 auto; padding-top: 120px; }

  .header { display: flex; justify-content: space-between; align-items: flex-end; height: 140px; }
  .brand { display: flex; flex-direction: column; gap: 10px; }
  .brand-name { font-family: "Open Sans", sans-serif; font-weight: 400; font-size: 46px; color: var(--ink); letter-spacing: 1px; line-height: 1; }
  .brand-tagline { font-family: "Open Sans", sans-serif; font-size: 15px; letter-spacing: .5px; text-transform: uppercase; color: var(--ink); }

  .header-tools { width: 600px; display: flex; flex-direction: column; gap: 14px; }
  .top-links { display: flex; justify-content: flex-end; gap: 34px; font-size: 12px; color: var(--muted); text-transform: uppercase; letter-spacing: .5px; }
  .top-links span { display: inline-flex; align-items: center; gap: 6px; }
  .tool-row { display: flex; justify-content: flex-end; align-items: flex-end; gap: 26px; }
  .search { width: 260px; border-bottom: 1px solid var(--muted); display: flex; justify-content: space-between; align-items: center; padding-bottom: 4px; font-size: 12px; color: var(--muted); }
  .search-go { width: 18px; height: 18px; background: var(--tan); display: grid; place-items: center; }
  .icon-link { display: flex; flex-direction: column; align-items: center; gap: 4px; font-size: 10px; color: var(--muted); text-transform: uppercase; }

  .nav { display: flex; background: var(--tan); margin-top: 8px; }
  .nav a { color: #fff; text-decoration: none; font-family: "Oswald", sans-serif; font-size: 15px; letter-spacing: .8px; padding: 10px 18px; border-right: 1px solid var(--tan-light); text-transform: uppercase; }
  .nav a:last-child { border-right: none; }

  .banner { position: relative; margin-top: 24px; height: 337px; background: linear-gradient(90deg, var(--blush) 0%, #f6e6e0 45%, var(--blush-deep) 100%); overflow: hidden; }
  .banner-copy { position: absolute; left: 60px; top: 78px; width: 500px; display: flex; flex-direction: column; align-items: center; }
  .banner-headline { font-family: "Oswald", sans-serif; font-weight: 700; font-size: 56px; line-height: 1; color: var(--crimson); text-transform: uppercase; letter-spacing: -1px; white-space: nowrap; }
  .banner-script { font-family: "Great Vibes", cursive; font-size: 50px; color: var(--crimson); line-height: 1; margin-top: 4px; white-space: nowrap; }
  .shop-now { margin-top: 34px; background: var(--crimson); color: #fff; font-family: "Oswald", sans-serif; font-size: 18px; padding: 5px 14px; text-transform: uppercase; }
  .banner-jewelry { position: absolute; left: 610px; top: 40px; width: 340px; height: 240px; border-radius: 48%; background: radial-gradient(ellipse at 65% 40%, #f0c24c 0%, #d8a53a 35%, #6e8a5a 60%, rgba(241,220,213,0) 75%); }
  .banner-band { position: absolute; left: 0; right: 0; bottom: 0; height: 26px; background: linear-gradient(180deg, var(--crimson) 0%, var(--crimson-dark) 100%); }

  .arrivals { margin-top: 28px; }
  .arrivals-bar { position: relative; height: 46px; background: var(--tan-light); display: grid; place-items: center; font-size: 19px; color: #fff; text-transform: uppercase; letter-spacing: .5px; }
  .view-all { position: absolute; right: 8px; top: 10px; background: var(--tan); color: #fff; font-size: 10px; padding: 6px 8px; }
  .carousel { position: relative; display: flex; padding: 0 20px; }
  .arrow { position: absolute; top: 110px; width: 18px; height: 40px; background: var(--tan-light); display: grid; place-items: center; }
  .arrow.prev { left: 0; } .arrow.next { right: 0; }
  .product { flex: 1; padding: 18px 14px 0; border-right: 1px solid #eee; text-align: center; }
  .product:last-child { border-right: none; }
  .product-title { font-size: 11px; color: var(--ink); height: 40px; }
  .product-photo { height: 150px; margin: 10px 16px 0; border-radius: 6px; }
  .photo-bangle { background: linear-gradient(160deg, #fafafa 20%, #c9a15a 50%, #3b3430 62%, #fafafa 80%); }
  .photo-serpent { background: radial-gradient(ellipse at center, #d7a38c 0%, #b96b52 45%, #fafafa 80%); }
  .photo-brooch { background: radial-gradient(ellipse at center, #d9dde0 0%, #9fb8a0 40%, #fafafa 78%); }
  .product-price { margin-top: 26px; font-size: 15px; color: var(--ink); }
</style>
</head>
<body>
  <svg class="sign-up-corner" viewBox="0 0 90 90" aria-label="Sign up">
    <polygon points="0,0 90,0 90,90" fill="var(--tan-light)"/>
    <text x="62" y="28" text-anchor="middle" font-family="Great Vibes, cursive" font-size="15" fill="var(--ink)" transform="rotate(45 62 28)">Sign Up!</text>
  </svg>

  <div class="site">
    <header class="header">
      <div class="brand">
        <div class="brand-name">Brindlestone</div>
        <div class="brand-tagline">Fine Estate and Designer Jewelry</div>
      </div>
      <div class="header-tools">
        <div class="top-links">
          <span><svg width="12" height="12" viewBox="0 0 24 24"><path d="M6 2l4 4-2 3c1 3 4 6 7 7l3-2 4 4-3 4C10 22 2 14 2 5z" fill="none" stroke="#8a8a8a" stroke-width="2"/></svg>800 - 555 - 0142</span>
          <span>Sell Jewelry</span>
          <span>Sign In / Register</span>
        </div>
        <div class="tool-row">
          <div class="search">Search<span class="search-go"><svg width="10" height="10" viewBox="0 0 10 10"><path d="M1 5l3 3 5-6" stroke="#fff" stroke-width="1.6" fill="none"/></svg></span></div>
          <div class="icon-link"><svg width="16" height="12" viewBox="0 0 16 12"><rect x="1" y="1" width="14" height="10" fill="none" stroke="#8a8a8a"/><path d="M1 1l7 6 7-6" fill="none" stroke="#8a8a8a"/></svg>Newsletter</div>
          <div class="icon-link"><svg width="16" height="14" viewBox="0 0 16 14"><path d="M8 13L2 7a3.5 3.5 0 016-4 3.5 3.5 0 016 4z" fill="none" stroke="#8a8a8a"/></svg>Wishlist</div>
          <div class="icon-link"><svg width="16" height="14" viewBox="0 0 16 14"><path d="M1 1h3l2 8h8l1-6H5" fill="none" stroke="#8a8a8a"/><circle cx="7" cy="12" r="1" fill="#8a8a8a"/><circle cx="13" cy="12" r="1" fill="#8a8a8a"/></svg>Cart (0)</div>
        </div>
        <nav class="nav">
          <a href="#">Fine Jewelry</a><a href="#">Timepieces</a><a href="#">Accessories</a><a href="#">Designers</a><a href="#">Sale</a>
        </nav>
      </div>
    </header>

    <section class="banner">
      <div class="banner-copy">
        <div class="banner-headline">Christmas is Closer</div>
        <div class="banner-script">Thank You Think Sale!</div>
        <div class="shop-now">Shop Now</div>
      </div>
      <div class="banner-jewelry" role="img" aria-label="Photo of gold cocktail rings set with colourful cabochon gemstones and diamonds"></div>
      <div class="banner-band"></div>
    </section>

    <section class="arrivals">
      <div class="arrivals-bar">New Arrivals<span class="view-all">VIEW ALL</span></div>
      <div class="carousel">
        <div class="arrow prev"><svg width="8" height="12" viewBox="0 0 8 12"><path d="M6 1L2 6l4 5" stroke="#fff" stroke-width="1.5" fill="none"/></svg></div>
        <div class="product">
          <div class="product-title">Lumina 6.00 Carat Fancy Diamond 18k Gold Bangle Bracelet</div>
          <div class="product-photo photo-bangle" role="img" aria-label="Photo of a wavy gold bangle bracelet set with dark diamonds"></div>
          <div class="product-price">$6,000</div>
        </div>
        <div class="product">
          <div class="product-title">Veloria Serpent Diamond Tourmaline 18 Karat Rose Gold Ring</div>
          <div class="product-photo photo-serpent" role="img" aria-label="Photo of a rose gold coiled serpent ring with diamonds and a tourmaline"></div>
          <div class="product-price">$8,800</div>
        </div>
        <div class="product">
          <div class="product-title">Art Deco Carved Emerald Ruby Diamond Platinum Brooch</div>
          <div class="product-photo photo-brooch" role="img" aria-label="Photo of an Art Deco platinum brooch with carved emeralds and rubies"></div>
          <div class="product-price">$2,600</div>
        </div>
        <div class="arrow next"><svg width="8" height="12" viewBox="0 0 8 12"><path d="M2 1l4 5-4 5" stroke="#fff" stroke-width="1.5" fill="none"/></svg></div>
      </div>
    </section>
  </div>
</body>
</html>
```